Business card and stationery for School
Business card and stationery for School - Education
Creative Brief
Use same font as used in my logo
However variations is permitted
Bright & Fun-filled
Mrs Belinda T. Marrowfield
Proprietress
Plot 418C QX4 Temberlo Layout Opposite Pinwick Office Halverton Road, Dosumi FCT, Abuja
info@bluepebbleacademy.example
www.bluepebbleacademy.example

```html
<!DOCTYPE html>
<html lang="en">
<head>
<meta charset="utf-8">
<title>Blue Pebble Academy – Business Card</title>
<link rel="stylesheet" href="https://fonts.googleapis.com/css2?family=Libre+Baskerville:ital,wght@0,400;0,700;1,400&family=Open+Sans:wght@400;600&display=swap">
<style>
  :root {
    --bg: #d9d9db;
    --card: #ffffff;
    --purple: #8a1f8c;
    --purple-light: #a43aa6;
    --green: #7db43a;
    --orange: #f39a1e;
    --grey: #6d6d6f;
  }
  * { margin: 0; padding: 0; box-sizing: border-box; }
  html, body { width: 1200px; height: 901px; overflow: hidden; }
  body {
    background: var(--bg);
    font-family: "Open Sans", Arial, sans-serif;
    position: relative;
  }
  .card {
    position: absolute;
    width: 620px;
    height: 354px;
    background: var(--card);
    border-radius: 14px;
    box-shadow: 0 6px 18px rgba(0,0,0,0.18);
    overflow: hidden;
  }
  /* back side */
  .card--back { left: 80px; top: 70px; }
  .back-mark {
    position: absolute;
    left: 0; right: 0; top: 110px;
    display: flex; align-items: center; justify-content: center; gap: 14px;
  }
  .back-mark .dot { width: 34px; height: 34px; border-radius: 50%; background: var(--green); }
  .back-mark .brand {
    font-family: "Libre Baskerville", Georgia, serif;
    font-weight: 700; font-size: 28px; color: var(--purple); letter-spacing: 1px;
  }
  .back-web {
    position: absolute; left: 0; right: 0; top: 200px;
    text-align: center; color: var(--grey); font-size: 15px; letter-spacing: 2px;
  }
  /* front side */
  .card--front { left: 500px; top: 470px; }
  .logo { position: absolute; left: 30px; top: 104px; width: 290px; }
  .logo .brand {
    display: flex; align-items: center; gap: 8px;
    font-family: "Libre Baskerville", Georgia, serif;
    font-weight: 700; font-size: 16px; color: var(--purple); letter-spacing: 0.3px;
    white-space: nowrap;
  }
  .logo .dot { width: 16px; height: 16px; border-radius: 50%; background: var(--green); flex: none; }
  .logo .tagline {
    margin: 5px 0 0 24px;
    font-family: "Libre Baskerville", Georgia, serif;
    font-style: italic; font-size: 11px; color: var(--green);
    border-top: 2px solid var(--green); padding-top: 2px; display: inline-block;
  }
  .contact { position: absolute; left: 340px; top: 58px; width: 265px; color: var(--grey); }
  .contact .name { font-size: 16px; color: var(--purple); }
  .contact .role { font-size: 12px; margin-top: 2px; }
  .contact .address { font-size: 12px; line-height: 1.35; margin-top: 16px; }
  .contact .lines { margin-top: 10px; font-size: 12px; line-height: 1.45; }
  .contact .line { display: flex; align-items: center; gap: 8px; white-space: nowrap; }
  .contact svg { width: 12px; height: 12px; fill: var(--purple); flex: none; }
  .rule { position: absolute; left: 0; right: 0; top: 262px; height: 3px; background: var(--purple); }
  .band { position: absolute; left: 0; right: 0; top: 276px; height: 40px; }
  .band .strip-left {
    position: absolute; left: 0; top: 0; width: 300px; height: 40px;
    background: var(--purple);
    color: #fff; font-size: 13px; line-height: 40px; padding-left: 30px; white-space: nowrap;
  }
  .band .strip-right {
    position: absolute; left: 386px; right: 0; top: 10px; height: 30px;
    background: var(--purple-light);
    color: #fff; font-size: 11px; line-height: 30px; text-align: right;
    padding-right: 16px; letter-spacing: 0.6px; white-space: nowrap;
  }
  .band svg { position: absolute; left: 296px; top: 0; }
</style>
</head>
<body>
  <section class="card card--back">
    <div class="back-mark">
      <span class="dot"></span>
      <span class="brand">BLUE PEBBLE ACADEMY</span>
    </div>
    <p class="back-web">www.bluepebbleacademy.example</p>
  </section>

  <section class="card card--front">
    <div class="logo">
      <div class="brand"><span class="dot"></span>BLUE PEBBLE ACADEMY</div>
      <span class="tagline">Learners today, Leaders tomorrow</span>
    </div>

    <div class="contact">
      <p class="name">Mrs Belinda T. Marrowfield</p>
      <p class="role">Proprietress</p>
      <p class="address">Plot 418C QX4 Temberlo Layout<br>Opposite Pinwick Office<br>Halverton Road, Dosumi<br>FCT, Abuja</p>
      <div class="lines">
        <p class="line"><svg viewBox="0 0 24 24"><path d="M6.6 10.8a15 15 0 0 0 6.6 6.6l2.2-2.2a1 1 0 0 1 1-.25 11.4 11.4 0 0 0 3.6.57 1 1 0 0 1 1 1V20a1 1 0 0 1-1 1A17 17 0 0 1 3 4a1 1 0 0 1 1-1h3.5a1 1 0 0 1 1 1c0 1.25.2 2.45.57 3.6a1 1 0 0 1-.25 1z"/></svg>+234 (09) 555 0142</p>
        <p class="line"><svg viewBox="0 0 24 24"><path d="M7 1h10a2 2 0 0 1 2 2v18a2 2 0 0 1-2 2H7a2 2 0 0 1-2-2V3a2 2 0 0 1 2-2zm0 4v13h10V5z"/></svg>+234 800 555 0199</p>
        <p class="line"><svg viewBox="0 0 24 24"><path d="M2 5h20v14H2zm2 2v.5l8 5 8-5V7z"/></svg>info@bluepebbleacademy.example</p>
      </div>
    </div>

    <div class="rule"></div>
    <div class="band">
      <div class="strip-left">Creche, Nursery, &amp; Primary School</div>
      <svg width="96" height="40" viewBox="0 0 96 40" aria-hidden="true">
        <polygon points="14,4 46,4 36,40 4,40" fill="var(--orange)"/>
        <polygon points="54,4 86,4 76,40 44,40" fill="var(--green)"/>
      </svg>
      <div class="strip-right">www.bluepebbleacademy.example</div>
    </div>
  </section>
</body>
</html>
```